Business car for dental practice

I have a new logo. Want it use for a new business card design. Hi end dental practice Would like a scan code on it for quick access to my web site and mobile site too. Green and purple are in logo design. Maybe have scan code on back? My website is peterhallwayDDS.example
Updates

Meadowlark Crest Dental Associates

482 N Tamarack Ln
Fernvale, NY 10597
914-555-0173

367 W Corliss Dr. 
Suite 584
Pine Hollow, NY 10596
914-555-0198

would like to incorporate logo, and addresses of both offices, and I recently saw a business card with a scan box on it which would bring people directly to the web site. if anyone knows how to do that, that could possibly go on the back of the card. (May be something I have to add at printing process) card can be one sided, or two sided.  

Reason: designer is revising for me. has not posted changes yet. hope he does soon!!

```html
<!DOCTYPE html>
<html lang="en">
<head>
<meta charset="utf-8">
<title>Meadowlark Crest Dental Associates – Business Card</title>
<link rel="stylesheet" href="https://fonts.googleapis.com/css2?family=Arimo:wght@400&display=swap">
<style>
  :root {
    --green: #529a42;
    --purple: #8a1c6c;
    --rule: #8c6b7c;
    --paper: #ffffff;
    --ink: #1f1f1f;
    --backdrop: #e9e6e1;
    --marker: #15322a;
  }
  * { box-sizing: border-box; margin: 0; padding: 0; }
  html, body { width: 1200px; height: 900px; overflow: hidden; }
  body {
    background: var(--backdrop);
    font-family: "Arimo", Arial, sans-serif;
    position: relative;
  }
  .card {
    position: absolute;
    background: var(--paper);
    overflow: hidden;
    box-shadow: 0 2px 6px rgba(0,0,0,.25);
  }
  .card--front { left: 44px; top: 34px; width: 700px; height: 400px; }
  .card--back  { left: 432px; top: 464px; width: 673px; height: 384px; }

  .band { position: absolute; left: 0; right: 0; background: var(--green); }
  .card--front .band { top: 208px; bottom: 0; }
  .card--back .band { top: 0; height: 190px; }

  .rule {
    position: absolute; height: 4px;
    border-top: 1px solid var(--rule);
    border-bottom: 1px solid var(--rule);
  }
  .card--front .rule--left  { top: 249px; left: 0; width: 140px; }
  .card--front .rule--right { top: 249px; left: 215px; right: 0; }
  .card--back .rule--left  { top: 116px; left: 0; width: 262px; }
  .card--back .rule--right { top: 116px; left: 330px; right: 0; }

  .brand { position: absolute; display: flex; align-items: flex-start; gap: 8px; }
  .brand__square { background: var(--purple); flex: none; }
  .brand__name {
    color: var(--purple);
    font-weight: 400;
    line-height: 1;
    white-space: nowrap;
  }
  .brand__line { display: block; }
  .brand__sub { display: block; letter-spacing: .4em; }

  .card--front .brand { left: 140px; top: 155px; }
  .card--front .brand__square { width: 75px; height: 75px; }
  .card--front .brand__line { font-size: 42px; margin-top: 10px; }
  .card--front .brand__sub { font-size: 19px; margin-top: 5px; }

  .card--back .brand { left: 262px; top: 142px; }
  .card--back .brand__square { width: 67px; height: 67px; }
  .card--back .brand__line { font-size: 37px; margin-top: 8px; }
  .card--back .brand__sub { font-size: 17px; margin-top: 4px; }

  .website {
    position: absolute; left: 0; right: 0; bottom: 10px;
    text-align: center; color: var(--paper); font-size: 15px;
  }

  .holder {
    position: absolute; left: 0; top: 203px;
    padding-left: 16px; font-size: 18px;
    border-left: 8px solid var(--marker);
    line-height: 18px;
  }
  .holder__first { color: var(--green); }
  .holder__last { color: var(--purple); }

  .contacts { position: absolute; left: 261px; top: 247px; list-style: none; }
  .contact {
    display: flex; align-items: center; gap: 12px;
    height: 22px; margin-bottom: 5.5px;
    font-size: 15px; color: var(--ink);
    white-space: nowrap;
  }
  .contact__icon { width: 22px; height: 22px; background: var(--purple); flex: none; }
</style>
</head>
<body>

<section class="card card--front" aria-label="Card front">
  <div class="band"></div>
  <div class="rule rule--left"></div>
  <div class="rule rule--right"></div>
  <div class="brand">
    <span class="brand__square"></span>
    <span class="brand__name">
      <span class="brand__line">Meadowlark Crest</span>
      <span class="brand__sub">Dental Associates</span>
    </span>
  </div>
  <p class="website">peterhallwayDDS.example</p>
</section>

<section class="card card--back" aria-label="Card back">
  <div class="band"></div>
  <div class="rule rule--left"></div>
  <div class="rule rule--right"></div>
  <div class="brand">
    <span class="brand__square"></span>
    <span class="brand__name">
      <span class="brand__line">Meadowlark Crest</span>
      <span class="brand__sub">Dental Associates</span>
    </span>
  </div>

  <p class="holder"><span class="holder__first">Name</span> <span class="holder__last">Surname</span></p>

  <ul class="contacts">
    <li class="contact">
      <svg class="contact__icon" viewBox="0 0 22 22" aria-hidden="true"><path d="M11 3.5a4.5 4.5 0 0 0-4.5 4.5c0 3.4 4.5 9.5 4.5 9.5s4.5-6.1 4.5-9.5A4.5 4.5 0 0 0 11 3.5zm0 6.3a1.8 1.8 0 1 1 0-3.6 1.8 1.8 0 0 1 0 3.6z" fill="#529a42"/></svg>
      <span>482 N Tamarack Ln, Fernvale, NY 10597</span>
    </li>
    <li class="contact">
      <svg class="contact__icon" viewBox="0 0 22 22" aria-hidden="true"><path d="M4 8c0-1.5 3-2.8 7-2.8S18 6.5 18 8v1.4h-3.2V8H7.2v1.4H4zM6.5 10.5h9l1.5 6H5z" fill="#529a42"/><circle cx="11" cy="13.5" r="1.6" fill="#8a1c6c"/></svg>
      <span>914 - 555 - 0173</span>
    </li>
    <li class="contact">
      <svg class="contact__icon" viewBox="0 0 22 22" aria-hidden="true"><path d="M11 3.5a4.5 4.5 0 0 0-4.5 4.5c0 3.4 4.5 9.5 4.5 9.5s4.5-6.1 4.5-9.5A4.5 4.5 0 0 0 11 3.5zm0 6.3a1.8 1.8 0 1 1 0-3.6 1.8 1.8 0 0 1 0 3.6z" fill="#529a42"/></svg>
      <span>367 W Corliss Dr. Suite 584 Pine Hollow, NY 10596</span>
    </li>
    <li class="contact">
      <svg class="contact__icon" viewBox="0 0 22 22" aria-hidden="true"><path d="M4 8c0-1.5 3-2.8 7-2.8S18 6.5 18 8v1.4h-3.2V8H7.2v1.4H4zM6.5 10.5h9l1.5 6H5z" fill="#529a42"/><circle cx="11" cy="13.5" r="1.6" fill="#8a1c6c"/></svg>
      <span>914-555-0198</span>
    </li>
  </ul>
</section>

</body>
</html>
```